Real Estate Open House & For Sale Signage

I am designing brand new signs for my real estate company. All I have so far are my logo and a business card design. I would like to have designed two different signs, 1. Open House directional sign, 2. For Sale Company sign. Both signs need to will be eye catching from the street, easy to read, identifiable and memorable.

Target Market(s)

Males & females, Ages between 30-65, affluent, educated, professionals.

Industry/Entity Type

Real Estate

Font styles to use
Serif
Sans Serif

Colors
33b8a4
34a7d8
acd137
3277b5

Requirements
Must have
• Must have my company logo & real estate license number visible on the sign. Must be easily visible and eye catching from a moving vehicle. Must have a professional and trustworthy appeal. Must bring to mind real estate.
Nice to have
• Image or icon that will denote real estate and be known as a part of my company identity and marketing theme.
Should not have
• Attached is a feeble attempt at creating my For Sale sign. The information on the sign is accurate, but the design is not appealing to me at all. It feels very amateurish.

```html
<!DOCTYPE html>
<html lang="en">
<head>
<meta charset="utf-8">
<title>For Sale Sign – Kailani Homes</title>
<link rel="stylesheet" href="https://fonts.googleapis.com/css2?family=Montserrat:wght@500;900&display=swap">
<style>
  :root {
    --brand-green: #7cbf2c;
    --brand-green-deep: #5a9e1f;
    --charcoal: #353131;
    --charcoal-edge: #222020;
    --paper: #ffffff;
    --photo-light: #d9dcdf;
    --photo-mid: #8c939a;
    --photo-skin: #e8b9a0;
  }
  html, body {
    margin: 0;
    padding: 0;
    width: 1200px;
    height: 900px;
    overflow: hidden;
    background: var(--paper);
  }
  .sign {
    display: block;
    width: 1200px;
    height: 900px;
  }
  .heavy {
    font-family: "Montserrat", Arial, sans-serif;
    font-weight: 900;
  }
  .brand-name { fill: var(--charcoal); font-size: 50px; }
  .brand-license {
    font-family: "Montserrat", Arial, sans-serif;
    font-weight: 500;
    font-size: 20px;
    fill: var(--charcoal);
  }
  .headline { fill: var(--paper); font-size: 192px; }
  .tagline { fill: var(--brand-green); font-size: 46px; }
  .agent { fill: var(--charcoal); font-size: 58px; }
  .phone { fill: var(--charcoal); font-size: 142px; }
</style>
</head>
<body>
<svg class="sign" viewBox="0 0 1200 900" xmlns="http://www.w3.org/2000/svg">
  <defs>
    <linearGradient id="photoTone" x1="0" y1="0" x2="1" y2="1">
      <stop offset="0" stop-color="var(--photo-light)"/>
      <stop offset="0.5" stop-color="var(--photo-mid)"/>
      <stop offset="1" stop-color="var(--photo-skin)"/>
    </linearGradient>
  </defs>

  <rect class="background" width="1200" height="900" fill="var(--paper)"/>

  <g class="brand">
    <rect class="brand-square" x="56" y="196" width="44" height="44" fill="var(--brand-green)"/>
    <text class="heavy brand-name" x="116" y="237">KAILANI HOMES</text>
    <text class="brand-license" x="58" y="284">License RB-30417</text>
  </g>

  <rect class="hero-photo" x="624" y="30" width="576" height="346" fill="url(#photoTone)" role="img" aria-label="Photo of a hand holding a small model house"/>

  <g class="band">
    <rect class="band-green" x="0" y="376" width="1200" height="334" fill="var(--brand-green)"/>
    <polygon class="band-charcoal-edge" points="596,376 1200,376 1200,544 644,544" fill="var(--charcoal-edge)"/>
    <polygon class="band-charcoal" points="614,376 1200,376 1200,544 664,544" fill="var(--charcoal)"/>
    <polygon class="band-accent" points="644,544 664,544 616,710 596,710" fill="var(--brand-green-deep)"/>
  </g>

  <text class="heavy headline" x="574" y="528" text-anchor="end" textLength="406" lengthAdjust="spacingAndGlyphs">FOR</text>
  <text class="heavy headline" x="570" y="694" text-anchor="end" textLength="518" lengthAdjust="spacingAndGlyphs">SALE</text>

  <g class="tagline-block">
    <text class="heavy tagline" x="674" y="433" textLength="140" lengthAdjust="spacingAndGlyphs">YOUR</text>
    <text class="heavy tagline" x="674" y="478" textLength="408" lengthAdjust="spacingAndGlyphs">NEIGHBORHOOD</text>
    <text class="heavy tagline" x="674" y="522" textLength="288" lengthAdjust="spacingAndGlyphs">SPECIALIST</text>
  </g>

  <g class="agent-block">
    <text class="heavy agent" x="676" y="618" textLength="472" lengthAdjust="spacingAndGlyphs">MAILE KANOA</text>
    <text class="heavy agent" x="676" y="676" textLength="290" lengthAdjust="spacingAndGlyphs">RB-21854</text>
  </g>

  <text class="heavy phone" x="56" y="840" textLength="1088" lengthAdjust="spacingAndGlyphs">808 555-0142</text>
</svg>
</body>
</html>
```